Thoroughbred Racing Partnership needs web design

Crest of Fortune Partners is a management group who buys horses and races them on both the West and East coasts. The premise of the business is for an investment as little as $500, anyone can be a partner and own a percentage of a horse(s). This is a low cost way of getting involved in the exciting sport of Thoroughbred Racing, without shouldering the heavy financial responsibility. Our target market is mostly males 40+ but we want to include all target markets. We are looking for something very clean and professional, we want to give an image of success. Nothing overly "artsy." I have included the logo in which you can incorporate in the site. Also, the logo colors will be the colors of our "silks." The silks are what the jockey wears and will be an important marketing tool for COF. We would like a very prominent picture of a racehorse somewhere on the homepage, we want to make it clear that is a website for Horseracing partnerships.

On the top of the site, it should say "Crest of Fortune" (on the top)
and below that "Thoroughbred Racing Partnerships." (below that)

The main sections, which should be across the top are:

Home
About Us
Ownership
Stable Roster
News
Contact us

Some of these will have drop down menus.

An example of a competitor website that we like is: www.harlowfieldeq.example
An example of a competitor website that we don't like is: www.gallopvane.example
Updates

Project Deadline Extended
Reason: We have a Board of Directors meeting on the 22nd and we will be making a decision on that day. I'm giving an extension so that all designers are able to submit their designs by the 22nd. Thank you!

Target Market(s)

40+ males

Industry/Entity Type

Business

Requirements
Must have
• our logo must be on the site. We would like at least one bold image of a thoroughbred horse in action. The picture is going to tell the story so it needs to be very eye-catching.

Our slogan should also be included on the website, "Experience the thrill of owning a Racehorse."
Should not have
• cartoons, artsy pictures, pictures of Steeplechase horses or "jumpers." This partnership is for racehorses only, there is not jumping involved with the horses.

```html
<!DOCTYPE html>
<html lang="en">
<head>
<meta charset="utf-8">
<title>Crest of Fortune - Thoroughbred Racing Partnerships</title>
<link rel="stylesheet" href="https://fonts.googleapis.com/css2?family=Crimson+Text:wght@400;600&family=Cinzel:wght@400&family=Jost:wght@500&family=Arimo:wght@400&display=swap">
<style>
  :root {
    --navy-bar: #0b2a5e;
    --navy: #1d4f8c;
    --banner-light: #0c4a8c;
    --banner-dark: #022a68;
    --panel: #eeebe5;
    --footer: #dcd9d4;
    --body-text: #1a1a1a;
    --footer-text: #5a5a5a;
    --rule: #c9c5bd;
    --turf: #6e9a45;
    --dirt: #a88463;
  }
  * { margin: 0; padding: 0; box-sizing: border-box; }
  html, body { width: 1200px; height: 1005px; overflow: hidden; }
  body { position: relative; background: var(--footer); font-family: "Arimo", Helvetica, Arial, sans-serif; }

  .track-backdrop {
    position: absolute; left: 0; top: 0; width: 1200px; height: 928px;
    background:
      linear-gradient(100deg, var(--dirt) 0%, #b8916c 8%, #8fae62 14%, var(--turf) 18%, #b08b66 24%, transparent 40%),
      linear-gradient(255deg, #86ad4e 0%, #7aa24a 14%, #e9e6df 20%, #b38f6b 26%, var(--dirt) 60%, #a07c5a 100%);
  }
  .top-bar { position: absolute; left: 0; top: 0; width: 1200px; height: 10px; background: var(--navy-bar); }

  .page-panel { position: absolute; left: 204px; top: 10px; width: 792px; height: 918px; background: var(--panel); }

  .brand-mark {
    position: absolute; left: 242px; top: 42px; width: 150px;
    font-family: "Crimson Text", Georgia, serif; font-weight: 600; color: var(--navy);
    font-size: 17.5px; line-height: 1; letter-spacing: 0;
  }
  .brand-mark .brand-dot { display: block; width: 40px; height: 40px; border-radius: 50%; background: var(--navy); margin-bottom: 10px; }

  .site-title {
    position: absolute; left: 415px; top: 39px; width: 545px; white-space: nowrap;
    font-family: "Crimson Text", Georgia, serif; font-weight: 400; font-size: 25.3px; line-height: 32px; color: var(--navy);
  }
  .main-nav { position: absolute; right: 242px; top: 96px; display: flex; gap: 12px; }
  .main-nav a { font-family: "Crimson Text", Georgia, serif; font-size: 17.5px; line-height: 24px; color: var(--navy); text-decoration: none; }

  .hero-banner {
    position: absolute; left: 241px; top: 140px; width: 721px; height: 160px; overflow: hidden;
    background: linear-gradient(90deg, var(--banner-light) 0%, #064087 55%, var(--banner-dark) 100%);
  }
  .hero-slogan {
    position: absolute; left: 38px; top: 44px;
    font-family: "Cinzel", "Times New Roman", serif; font-size: 30px; line-height: 36px;
    color: #ffffff; letter-spacing: 1.5px;
  }

  .section-heading {
    position: absolute; left: 271px;
    font-family: "Jost", "Futura", sans-serif; font-weight: 500; font-size: 14.5px; line-height: 18px; color: var(--navy);
    letter-spacing: 0.4px; text-transform: uppercase;
  }
  .about-heading { top: 342px; }
  .horses-heading { top: 736px; }

  .about-copy { position: absolute; left: 273px; top: 370px; width: 652px; }
  .about-copy p { font-size: 12px; line-height: 18px; letter-spacing: -0.05px; color: var(--body-text); text-align: justify; margin-bottom: 18px; }

  .divider { position: absolute; left: 270px; width: 654px; height: 1px; background: var(--rule); }
  .divider-upper { top: 719px; }
  .divider-lower { top: 892px; }

  .horse-photo { position: absolute; top: 765px; width: 147px; height: 111px; }
  .horse-1 { left: 271px; background: linear-gradient(180deg, #6f7e58 0%, #8a6040 45%, #5d8a3c 100%); }
  .horse-2 { left: 438px; background: linear-gradient(180deg, #c8473a 0%, #3a2a22 50%, #7c8a3c 100%); }
  .horse-3 { left: 608px; background: linear-gradient(180deg, #3a2a1e 0%, #a5552c 50%, #6a3a22 100%); }
  .horse-4 { left: 778px; background: linear-gradient(180deg, #b5a58a 0%, #9c5a34 50%, #c9b59a 100%); }

  .site-footer { position: absolute; left: 0; top: 928px; width: 1200px; height: 77px; background: var(--footer); }
  .footer-nav { position: absolute; left: 241px; top: 22px; font-size: 11px; line-height: 14px; color: var(--footer-text); }
  .footer-nav a { color: var(--footer-text); text-decoration: none; }
  .footer-nav .sep { margin: 0 5px; }
  .copyright { position: absolute; left: 241px; top: 37px; font-size: 11px; line-height: 14px; color: var(--footer-text); }
  .social-links { position: absolute; left: 795px; top: 31px; display: flex; gap: 11px; }
  .social-links span { width: 25px; height: 25px; border-radius: 50%; display: block; }
  .social-a { background: #3aa3dd; }
  .social-b { background: #3c5a96; }
  .social-c { background: #f4f4f4; border: 1px solid #bdbdbd; }
  .social-d { background: #f08a1c; }
</style>
</head>
<body>
  <div class="track-backdrop" role="img" aria-label="Aerial photo of a curving racetrack with dirt surface, white rails, turf and a lone horse and rider galloping"></div>
  <div class="top-bar"></div>
  <div class="page-panel"></div>

  <div class="brand-mark"><span class="brand-dot"></span>COFPARTNERS.COM</div>
  <h1 class="site-title">Crest of Fortune - Thoroughbred Racing Partnerships</h1>
  <nav class="main-nav">
    <a href="#">Home</a><a href="#">About Us</a><a href="#">Ownership</a><a href="#">Stable Roster</a><a href="#">News</a><a href="#">Contact us</a>
  </nav>

  <section class="hero-banner">
    <p class="hero-slogan">Experience the thrill<br>of owning a Racehorse</p>
  </section>

  <h2 class="section-heading about-heading">About Us</h2>
  <div class="about-copy">
    <p>Lorem ipsum dolor sit amet, consectetur adipiscing elit. Nulla ultricies dignissim convallis. Vestibulum varius congue urna, non scelerisque turpis gravida viverra. Curabitur euismod ut massa ut scelerisque. Proin pharetra congue justo a lacinia. Integer vel erat aliquam nibh commodo tristique. Aliquam eu mi a arcu aliquet pretium. Aliquam malesuada urna sed consectetur eleifend.</p>
    <p>Suspendisse potenti. Ut molestie porttitor dolor, eu varius tellus vehicula faucibus. Curabitur feugiat arcu at sagittis dictum. Pellentesque tempor fringilla congue. Vivamus sit amet scelerisque mauris, a pharetra lectus. Maecenas pellentesque diam vel sapien facilisis mollis. Aliquam ornare, diam at rhoncus lacinia, diam risus rutrum dolor, sit amet consequat leo purus eget arcu. Pellentesque tempus neque vel venenatis eleifend. Fusce lorem diam, convallis a lorem ut, sagittis fermentum augue. Etiam pulvinar faucibus purus, eu scelerisque purus vulputate id. Donec tincidunt justo a vulputate interdum.</p>
    <p>Nam vel sagittis tortor. Quisque leo magna, posuere ac tellus vel, laoreet dapibus lorem. Donec cursus semper nisl a viverra. Phasellus tristique dolor faucibus libero sollicitudin consequat. Nulla nisi lectus, venenatis nec orci non, tristique facilisis enim. Phasellus bibendum enim risus, sit amet adipiscing tellus elementum quis. Suspendisse rhoncus lectus nec augue rutrum dapibus. Vestibulum placerat placerat est, eget tempor nibh tristique at. Donec sit amet turpis urna. In at augue id justo laoreet faucibus a vitae risus. Donec lorem neque, sollicitudin non vehicula vel, luctus in metus. Vestibulum nec bibendum massa, iaculis hendrerit arcu. Proin quis hendrerit purus. Vestibulum cursus lectus orci, sit amet elementum tellus aliquet ut. Nam lacinia ipsum eu justo pellentesque egestas.</p>
  </div>

  <div class="divider divider-upper"></div>
  <h2 class="section-heading horses-heading">Our Horses</h2>
  <div class="horse-photo horse-1" role="img" aria-label="Chestnut racehorse and jockey galloping on turf"></div>
  <div class="horse-photo horse-2" role="img" aria-label="Dark bay racehorse and jockey at full stride past the rail"></div>
  <div class="horse-photo horse-3" role="img" aria-label="Two chestnut racehorses racing neck and neck under lights"></div>
  <div class="horse-photo horse-4" role="img" aria-label="Chestnut racehorse and jockey in pink silks on the dirt"></div>
  <div class="divider divider-lower"></div>

  <footer class="site-footer">
    <div class="footer-nav">
      <a href="#">Home</a><span class="sep">|</span><a href="#">About Us</a><span class="sep">|</span><a href="#">Ownership</a><span class="sep">|</span><a href="#">Stable Rooster</a><span class="sep">|</span><a href="#">News</a><span class="sep">|</span><a href="#">Contact</a>
    </div>
    <p class="copyright">© 2013 Marlowe. All Rights Reserved</p>
    <div class="social-links" aria-label="Social links">
      <span class="social-a"></span><span class="social-b"></span><span class="social-c"></span><span class="social-d"></span>
    </div>
  </footer>
</body>
</html>
```